Packaging Design for Dates Products Exports

We are exporters of Dates products globally - company name is Crescent Orchard Provisions LLC.

We are looking to revamp our boxes packaging - I have attached our preliminary logo.

Our color palette is predominantly dark green and gold. Packaging can include shades of black, dark red, beige - I have included another very preliminary sample for clarity.

Note please we are looking for substantially better designs than both attached pictures. Our products are of premium quality and would want our packaging to reflect that. Please be inspired by Dates products packaging of global suppliers as well to get a sense of industry-specific themes.

Packaging size is 430mm length, 150mm width, 280mm height.

Target Market(s)

Dates products wholesale importers in Asia, Europe, US, Australia, etx

Industry/Entity Type

Dates Products

Font styles to use
Decorative
Script

Colors

Designer to choose colors to be used in the design.

Requirements
Must have
• Premium look and feel reflecting product quality, company & industry-specific color palette/design themes that are relevant

```html
<!DOCTYPE html>
<html lang="en">
<head>
<meta charset="utf-8">
<title>Crescent Orchard Premium Dates – Carton Panels</title>
<link href="https://fonts.googleapis.com/css2?family=Cinzel:wght@500;600;700&family=Amiri:wght@700&family=Tiro+Devanagari+Hindi&display=swap" rel="stylesheet">
<style>
  :root {
    --page: #cfcfcf;
    --green-deep: #0a3a20;
    --green: #114a2b;
    --green-light: #1b5e38;
    --gold: #d4a93a;
    --gold-light: #f0cf6e;
    --gold-dark: #9c7420;
    --ivory: #f4f3f1;
    --white: #ffffff;
    --brand-green: #1d6b3a;
  }
  * { margin: 0; padding: 0; box-sizing: border-box; }
  html, body { width: 1200px; height: 800px; overflow: hidden; }
  body { background: var(--page); font-family: "Cinzel", serif; position: relative; }

  .panel {
    position: absolute; overflow: hidden;
    background: var(--green);
    box-shadow: 0 6px 18px rgba(0,0,0,.22);
  }
  .pattern {
    position: absolute; inset: 0;
    background:
      radial-gradient(circle at 30% 30%, rgba(255,255,255,.06), transparent 40%),
      radial-gradient(circle at 75% 70%, rgba(255,255,255,.05), transparent 45%),
      radial-gradient(ellipse at 55% 45%, var(--green-light), var(--green) 55%, var(--green-deep));
  }

  /* ---------- Lid ---------- */
  .lid { left: 40px; top: 20px; width: 740px; height: 440px; }
  .lid .ivory-band {
    position: absolute; left: 0; top: 0; width: 200px; height: 100%;
    background: var(--ivory);
    border-right: 4px solid var(--gold);
  }
  .lid .ivory-band::after {
    content: ""; position: absolute; right: 5px; top: 0; bottom: 0;
    border-right: 1px solid var(--gold-dark);
  }
  .brand-mark {
    position: absolute; top: 28px; left: 0; width: 100%;
    display: flex; flex-direction: column; align-items: center; gap: 7px;
  }
  .brand-mark .dot {
    width: 34px; height: 34px; border-radius: 50%;
    border: 3px solid var(--brand-green);
  }
  .brand-mark .name {
    font-weight: 600; font-size: 11px; letter-spacing: .8px;
    color: var(--brand-green); text-align: center; line-height: 1.4;
  }
  .scene-art {
    position: absolute; left: 26px; top: 130px; width: 168px; height: 250px;
    border-radius: 84px 84px 0 0;
    background: linear-gradient(180deg, #5a4a2a 0%, #b08a3a 45%, #d9b55a 70%, #2c3b35 100%);
    border: 2px solid var(--gold-dark);
  }

  .lid-titles {
    position: absolute; left: 204px; width: 536px; top: 18px; text-align: center;
  }
  .title-ar {
    font-family: "Amiri", serif; font-weight: 700; color: var(--gold-light); line-height: 1.15;
  }
  .title-brand { font-weight: 600; color: var(--white); letter-spacing: 1.5px; line-height: 1.1; }
  .title-premium {
    display: flex; justify-content: center; align-items: center;
    font-weight: 600; color: var(--gold); letter-spacing: 2px; line-height: 1.2;
  }
  .pip { background: var(--gold); transform: rotate(45deg); display: inline-block; }
  .title-product { font-weight: 500; color: var(--white); letter-spacing: 3px; line-height: 1; }

  .lid .title-ar { font-size: 30px; }
  .lid .title-brand { font-size: 29px; }
  .lid .title-premium { font-size: 24px; gap: 14px; }
  .lid .pip { width: 10px; height: 10px; }
  .lid .title-product { font-size: 84px; }

  .product-window {
    position: absolute; left: 340px; top: 232px; width: 264px; height: 138px;
    border: 3px solid var(--gold); border-radius: 22px;
    outline: 1px solid var(--gold-light); outline-offset: 4px;
    background: radial-gradient(ellipse at 50% 50%, #6b2a22, #3a1a18 60%, #1f0f10);
  }
  .name-strip {
    position: absolute; left: 204px; width: 536px; top: 388px;
    display: flex; justify-content: center; align-items: baseline; gap: 16px;
    color: var(--gold); font-weight: 700; font-size: 20px; letter-spacing: 1.5px;
  }
  .name-strip .hi { font-family: "Tiro Devanagari Hindi", serif; font-weight: 400; font-size: 23px; }
  .name-strip .ar { font-family: "Amiri", serif; font-size: 24px; }

  .weight-tag {
    position: absolute; right: 14px; top: 14px; width: 66px; height: 66px;
    border-radius: 50%; background: var(--white);
    display: flex; flex-direction: column; align-items: center; justify-content: center;
    color: var(--green-deep); font-weight: 700;
  }
  .weight-tag .num { font-size: 30px; line-height: 1; }
  .weight-tag .unit { font-size: 11px; }

  /* ---------- Front ---------- */
  .front { left: 40px; top: 470px; width: 740px; height: 310px; }
  .front .ivory-band {
    position: absolute; left: 40px; top: 0; width: 150px; height: 100%;
    background: var(--ivory);
    border-left: 3px solid var(--gold); border-right: 3px solid var(--gold);
  }
  .seal {
    position: absolute; left: 25px; top: 100px; width: 100px; height: 100px;
    border-radius: 50%; border: 6px solid var(--brand-green);
  }
  .front-titles {
    position: absolute; left: 190px; width: 550px; top: 34px; text-align: center;
  }
  .front .title-ar { font-size: 32px; }
  .front .title-brand { font-size: 32px; }
  .front .title-premium { font-size: 26px; gap: 14px; }
  .front .pip { width: 10px; height: 10px; }
  .front .title-product { font-size: 92px; }

  /* ---------- End ---------- */
  .end { left: 790px; top: 470px; width: 370px; height: 310px; }
  .end-info {
    position: absolute; left: 20px; top: 26px; width: 160px; bottom: 22px;
    display: flex; flex-direction: column; justify-content: space-between;
    color: var(--white);
  }
  .end-info .copy { font-family: Georgia, serif; font-size: 9.5px; line-height: 1.5; opacity: .9; }
  .end-info .facts { font-family: Georgia, serif; font-size: 10px; letter-spacing: .5px; line-height: 1.8; }
  .end-titles {
    position: absolute; left: 190px; width: 170px; top: 62px; text-align: center;
  }
  .end .title-ar { font-size: 22px; }
  .end .title-brand { font-size: 15px; letter-spacing: .5px; }
  .end .title-premium { font-size: 15px; gap: 8px; }
  .end .pip { width: 6px; height: 6px; }
  .end .title-product { font-size: 44px; letter-spacing: 1px; margin-top: 2px; }
</style>
</head>
<body>
  <main class="lid panel">
    <div class="pattern" role="img" aria-label="Faint interlaced geometric star pattern in dark green"></div>
    <aside class="ivory-band">
      <div class="brand-mark">
        <span class="dot"></span>
        <span class="name">CRESCENT ORCHARD<br>PROVISIONS LLC</span>
      </div>
      <div class="scene-art" role="img" aria-label="Illustration of a family sharing dates at an iftar table beneath an arched window with a hanging lantern"></div>
    </aside>

    <section class="lid-titles">
      <p class="title-ar" lang="ar">بستان الهلال</p>
      <h1 class="title-brand">CRESCENT ORCHARD</h1>
      <p class="title-premium"><span class="pip"></span>PREMIUM<span class="pip"></span></p>
      <p class="title-product">DATES</p>
    </section>

    <div class="product-window" role="img" aria-label="Photograph of glossy premium Medjool dates"></div>

    <p class="name-strip">
      <span>DATTES</span>
      <span class="hi" lang="hi">खजूर</span>
      <span class="ar" lang="ar">تمر</span>
      <span>DATES</span>
    </p>

    <div class="weight-tag"><span class="num">5</span><span class="unit">KG</span></div>
  </main>

  <section class="front panel">
    <div class="pattern" role="img" aria-label="Faint interlaced geometric star pattern in dark green"></div>
    <div class="ivory-band"><span class="seal"></span></div>
    <div class="front-titles">
      <p class="title-ar" lang="ar">بستان الهلال</p>
      <p class="title-brand">CRESCENT ORCHARD</p>
      <p class="title-premium"><span class="pip"></span>PREMIUM<span class="pip"></span></p>
      <p class="title-product">DATES</p>
    </div>
  </section>

  <section class="end panel">
    <div class="pattern" role="img" aria-label="Faint interlaced geometric star pattern in dark green"></div>
    <div class="end-info">
      <p class="copy">Carefully selected premium dates, hand sorted and packed under strict hygiene standards. Store in a cool, dry place away from direct sunlight. Best enjoyed within twelve months of packing. Naturally sweet with no added sugar or preservatives.</p>
      <p class="facts">MADE IN U.A.E<br>NET WEIGHT: 5 KG</p>
    </div>
    <div class="end-titles">
      <p class="title-ar" lang="ar">بستان الهلال</p>
      <p class="title-brand">CRESCENT ORCHARD</p>
      <p class="title-premium"><span class="pip"></span>PREMIUM<span class="pip"></span></p>
      <p class="title-product">DATES</p>
    </div>
  </section>
</body>
</html>
```